New Innovative Product needs a new business card design

We need a business card design for a new product line based in Michigan called "Lender TrueCourse." We are a credit company by nature however this product should have a clean, simple, "zorvel-esque" feel. We have a few tag lines we use that could or could not be used...."All Referral Roads Lead to You" we use the attached pic in much or our marketing and also use both a white and/or black logo. Also attached.

We want the image attached on the card in some form or another- the grass/sky image.

Reason: We are extending to go over options with management- (expiring on weekend)

Reason: To finalize our design pick. We will be in touch with the designer of choice within the next day or so...the last few entries have been great- Sorry for the delay.

Reason: Working with a couple different designs trying to get finalized

Reason: Final in the workds

Industry/Entity Type

Marketing

Requirements
Must have
• We want the image attached on the card in some form or another- the grass/sky image.

```html
<!DOCTYPE html>
<html lang="en">
<head>
<meta charset="utf-8">
<title>Lender TrueCourse – Business Card</title>
<link rel="stylesheet" href="https://fonts.googleapis.com/css2?family=Exo+2:wght@300;400;600;800&display=swap">
<style>
  :root {
    --page: #e9e9e7;
    --sky-deep: #2f5f9e;
    --sky-light: #9cc1e6;
    --grass: #5fae2a;
    --grass-dark: #3f8a1c;
    --ink: #111111;
    --white: #ffffff;
    --brand-green: #4aa54f;
    --rule: rgba(255,255,255,0.7);
  }
  * { box-sizing: border-box; margin: 0; padding: 0; }
  html, body { width: 1200px; height: 900px; overflow: hidden; }
  body {
    background: var(--page);
    font-family: "Exo 2", sans-serif;
    color: var(--ink);
    position: relative;
  }
  .card {
    position: absolute;
    left: 285px;
    width: 630px;
    height: 360px;
    overflow: hidden;
    background: var(--white);
    box-shadow: 0 6px 20px rgba(0,0,0,0.18);
  }
  .card--front { top: 50px; }
  .card--back { top: 490px; }

  .field-photo {
    position: absolute;
    inset: 0;
    background: linear-gradient(160deg, var(--sky-deep) 0%, var(--sky-light) 45%, var(--grass) 62%, var(--grass-dark) 100%);
  }
  .card--back .field-photo { top: 110px; }

  .brand {
    position: absolute;
    display: flex;
    align-items: center;
    gap: 10px;
  }
  .brand__mark {
    width: 34px; height: 34px;
    background: var(--brand-green);
  }
  .brand__name {
    font-weight: 600;
    font-size: 22px;
    line-height: 1;
    color: var(--white);
  }
  .card--front .brand { top: 22px; right: 26px; }
  .card--back .brand { top: 38px; right: 40px; }
  .card--back .brand__name { color: var(--ink); }

  .name-band {
    position: absolute;
    left: 0; right: 0;
    top: 120px;
    height: 70px;
    background: rgba(255,255,255,0.55);
  }
  .person__name {
    position: absolute;
    left: 34px; top: 124px;
    font-weight: 800;
    font-size: 54px;
    line-height: 62px;
    letter-spacing: 1px;
    color: var(--ink);
  }
  .person__title {
    position: absolute;
    right: 40px; top: 197px;
    font-weight: 400;
    font-size: 18px;
    line-height: 22px;
    color: var(--ink);
  }

  .contact {
    position: absolute;
    left: 34px; bottom: 16px;
    list-style: none;
    color: var(--white);
    font-size: 13px;
    line-height: 15px;
    border-left: 1px solid var(--rule);
    padding-left: 0;
  }
  .contact__item {
    display: flex;
    align-items: center;
    gap: 10px;
    min-height: 22px;
    margin-left: -1px;
  }
  .contact__item--address { margin-bottom: 4px; }
  .contact__icon {
    width: 18px; height: 18px;
    flex: none;
  }

  .tagline {
    position: absolute;
    left: 60px; bottom: 30px;
    font-weight: 300;
    font-size: 40px;
    line-height: 1.05;
    color: var(--ink);
  }
  .tagline__line { display: block; }
  .tagline__line--second { padding-left: 150px; }
</style>
</head>
<body>

<section class="card card--front" aria-label="Business card front">
  <div class="field-photo" role="img" aria-label="Photo of a green grass field under a blue sky with white clouds"></div>

  <div class="brand">
    <span class="brand__mark"></span>
    <span class="brand__name">Lender TrueCourse</span>
  </div>

  <div class="name-band"></div>
  <h1 class="person__name">Colin Marsh</h1>
  <p class="person__title">Product Manager</p>

  <ul class="contact">
    <li class="contact__item contact__item--address">
      <svg class="contact__icon" viewBox="0 0 18 18"><circle cx="9" cy="9" r="8.5" fill="#fff"/><path d="M9 4a3 3 0 0 0-3 3c0 2.2 3 6 3 6s3-3.8 3-6a3 3 0 0 0-3-3z" fill="#3f8a1c"/><circle cx="9" cy="7" r="1" fill="#fff"/></svg>
      <span>2210 W. Meadow Rd.<br>Lansing, MI 48906</span>
    </li>
    <li class="contact__item">
      <svg class="contact__icon" viewBox="0 0 18 18"><circle cx="9" cy="9" r="8.5" fill="#fff"/><path d="M6 5l2 0 1 2.5-1.2.8a6 6 0 0 0 2.9 2.9l.8-1.2 2.5 1v2c-4.5.3-8.3-3.5-8-8z" fill="#3f8a1c"/></svg>
      <span>555.214.0187</span>
    </li>
    <li class="contact__item">
      <svg class="contact__icon" viewBox="0 0 18 18"><circle cx="9" cy="9" r="8.5" fill="#fff"/><text x="9" y="12.5" font-size="10" text-anchor="middle" fill="#3f8a1c" font-family="sans-serif">@</text></svg>
      <span>cmarsh@truecoursecredit.com</span>
    </li>
    <li class="contact__item">
      <svg class="contact__icon" viewBox="0 0 18 18"><circle cx="9" cy="9" r="8.5" fill="#fff"/></svg>
      <span>@cmarshcredit</span>
    </li>
    <li class="contact__item">
      <svg class="contact__icon" viewBox="0 0 18 18"><circle cx="9" cy="9" r="8.5" fill="#fff"/></svg>
      <span>cmarsh.truecourse</span>
    </li>
  </ul>
</section>

<section class="card card--back" aria-label="Business card back">
  <div class="brand">
    <span class="brand__mark"></span>
    <span class="brand__name">Lender TrueCourse</span>
  </div>

  <div class="field-photo" role="img" aria-label="Photo of a green grass field under a blue sky with white clouds"></div>

  <p class="tagline">
    <span class="tagline__line">All referral roads</span>
    <span class="tagline__line tagline__line--second">lead to you</span>
  </p>
</section>

</body>
</html>
```